Exciting New Reseller Brand requires Website to WOW New clients to register.

We are a NEW online business called Trade Our Goods.

The Website is a simple concept, it looks to put Merchants (businesses that want their products resold) in touch with Resellers (people or businesses that want to resell that product).

The website acts as an online market place which looks to get Merchants to sign-up and pay to list their company and product as well as getting Resellers to sign-up to view potential Merchants they can get in touch with in the right industry or area to resell their products for (see attached slide-pack to explain packages)

Any type of Industry or Business can register themselves to get listed on Trade Our Goods to see either get their product/service resold or to look for products / services to reseller.

Trade Our Goods does not take any other monetary part in the business relationships other than to obtain money for the monthly website subscription.

We want a very simple website, so this project is for several pages:

Page 1) A really vibrant, exciting, image based homepage to get people to sign-up / register (see sites that we like in the project brief). Needs to be very clear that there are 2 customers and to sign up to join, build and earn!

Page 2) A page that describes the benefits and packages for Resellers.

Page 3) A page that describes the benefits and packages for Merchants.

Page 4) The Payment process pages, taking the customer through sign-up

Page 5) The Business Listings page, so when people search for a Merchant how this will be displayed.

We would really like an image based site and preferably parallax. We want it bright vibrant and to look like a social media site.

All necessary files / logos enclosed.

We would love to continue to work with the winning designer moving forward.

Many thanks and Good Luck.

Regards

Martin & Owen

Target Market(s)

Merchants, Suppliers, Vendors, Manufacturers, Distributors, Wholesalers, Affiliate programs, Franchisees, Reselers

Industry/Entity Type

Business

Number of Pages Required

5+ page

Requirements
Must have
• We love the following websites:
• 1) Like the top section, i.e. parallax image based: www.brightkitestudio.co.uk
• 2) Like the way the screen is split in 2, could be used to describe the 2 different customers we are after Merchants / Resellers: www.filevault-example.com/guide
• 3) Like the bright colours / full screen video split into 2 below top banner and the generally how simple the site is: www.harbourlinden.com.au
• 4) Love all of this site, simple, bold, Love the colours, the clear message and the infographics: http://www.velorin-example.com/swiftrider/faster

```html
<!DOCTYPE html>
<html lang="en">
<head>
<meta charset="utf-8">
<title>Trade Our Goods – Join, Build, Earn</title>
<link href="https://fonts.googleapis.com/css2?family=Open+Sans:wght@300;400;600;700&display=swap" rel="stylesheet">
<style>
:root{
  --blue:#1a8fd6;
  --blue-deep:#0f6fb3;
  --green:#8cc63f;
  --green-deep:#79b22f;
  --ink:#333333;
  --muted:#7d7d7d;
  --line:#d9d9d9;
  --grey-band:#efefef;
  --dark:#1f1f1f;
  --white:#ffffff;
}
*{box-sizing:border-box;margin:0;padding:0}
html,body{width:1200px;height:5070px;overflow:hidden}
body{font-family:"Open Sans",Arial,sans-serif;color:var(--ink);background:var(--white);position:relative}
.section{position:absolute;left:0;width:1200px}
.center{text-align:center}
.abs{position:absolute}

/* header / hero */
.hero{top:0;height:620px;background:linear-gradient(180deg,#1c2229 0%,#2d3640 45%,#171c22 100%)}
.hero-photo{position:absolute;inset:0;background:radial-gradient(ellipse at 55% 60%,rgba(120,130,140,.35),rgba(0,0,0,0) 60%)}
.brand{position:absolute;left:160px;top:28px;display:flex;align-items:center;gap:10px;color:var(--white);font-weight:700;font-size:28px;letter-spacing:-.3px}
.brand-dot{width:34px;height:34px;border-radius:50%;background:var(--white)}
.nav{position:absolute;right:150px;top:52px;display:flex;gap:34px;font-size:14px;color:var(--white)}
.nav .active{border-bottom:2px solid var(--white);padding-bottom:6px}
.hero-kicker{position:absolute;top:296px;width:100%;text-align:center;color:var(--white);font-weight:300;font-size:34px;letter-spacing:1px}
.hero-title{position:absolute;top:352px;width:100%;text-align:center;color:var(--white);font-weight:700;font-size:52px;letter-spacing:2px}
.hero-title .sep{color:var(--green);font-weight:400;margin:0 6px}

/* split */
.split-band{top:620px;height:310px;background:var(--grey-band)}
.split{position:absolute;top:585px;left:142px;width:916px;height:270px;display:flex}
.split-card{flex:1;text-align:center;color:var(--white);padding-top:45px}
.split-card.merchants{background:var(--blue)}
.split-card.resellers{background:var(--green)}
.split-card h2{font-size:50px;font-weight:700;letter-spacing:1px;line-height:1}
.split-card p{font-size:19px;margin-top:18px}
.split-btn{display:inline-block;margin-top:24px;width:176px;height:46px;line-height:42px;border:2px solid var(--white);font-size:14px;font-weight:600}

/* headings + divider */
.h-section{font-size:56px;font-weight:600;color:var(--ink);letter-spacing:1px}
.divider{position:relative;width:190px;height:20px;margin:0 auto}
.divider::before{content:"";position:absolute;left:0;right:0;top:10px;height:1px;background:var(--line)}
.divider span{position:absolute;left:85px;top:0;width:20px;height:20px;border-radius:50%;border:4px solid var(--blue);border-right-color:var(--green);border-bottom-color:var(--green);background:var(--white)}
.divider.on-dark::before{background:#666}
.divider.on-dark span{border-color:var(--white);background:transparent}
.divider.on-blue::before{background:rgba(255,255,255,.5)}
.divider.on-blue span{border-color:var(--white);background:var(--blue)}

/* what we do */
.what{top:930px;height:432px}
.what .h-section{position:absolute;top:78px;width:100%}
.what .divider{position:absolute;top:1092px;left:505px;top:162px}
.what-sub{position:absolute;top:207px;width:100%;color:var(--blue);font-size:20px;font-weight:600}
.what-body{position:absolute;top:258px;left:152px;width:896px;font-size:16px;line-height:27px;color:var(--muted);text-align:center}

/* why */
.why{top:1362px;height:406px;background:linear-gradient(90deg,#ececec,#f6f6f6)}
.why-photo{position:absolute;right:0;top:0;width:642px;height:406px;background:linear-gradient(135deg,#f2f2f2 0%,#dcdcdc 55%,#b7b0a6 100%)}
.why h2{position:absolute;left:142px;top:58px;font-size:42px;font-weight:400;color:var(--ink)}
.why-sub{position:absolute;left:142px;top:124px;color:var(--blue);font-size:18px;font-weight:600}
.why-list{position:absolute;left:142px;top:170px;list-style:none;font-size:16px;line-height:27px;color:var(--muted)}

/* blog */
.blog{top:1768px;height:649px}
.blog .h-section{position:absolute;top:104px;width:100%}
.blog .divider{position:absolute;left:505px;top:182px}
.post{position:absolute;top:263px;width:281px;height:257px;background:#f4f4f4}
.post-photo{height:190px;background:linear-gradient(160deg,#c9d3dc,#8a97a3)}
.post-bar{background:var(--green);color:var(--white);padding:10px 12px;height:67px}
.post-bar h3{font-size:13px;font-weight:700}
.post-meta{display:flex;gap:22px;font-size:12px;margin-top:9px}
.dots{position:absolute;top:580px;width:100%;display:flex;justify-content:center;gap:12px}
.dots i{width:9px;height:9px;border-radius:50%;background:#cfcfcf;display:block}
.dots i.on{background:var(--blue)}

/* how it works */
.how{top:2417px;height:642px;background:linear-gradient(180deg,#2b2b2b,#1a1a1a)}
.how .h-section{position:absolute;top:72px;width:100%;color:var(--white)}
.how .divider{position:absolute;left:505px;top:158px}
.how-body{position:absolute;top:218px;left:210px;width:780px;text-align:center;color:var(--white);font-size:14px;line-height:24px}
.hex-row{position:absolute;top:0;left:0;width:1200px;height:642px}
.hex-label{position:absolute;top:494px;width:120px;margin-left:-60px;text-align:center;color:var(--white);font-size:14px}

/* benefits */
.benefits{top:3059px;height:659px}
.benefits .h-section{position:absolute;top:102px;width:100%}
.benefits .divider{position:absolute;left:505px;top:203px}
.ribbon{position:absolute;top:277px;left:0;width:1200px;height:68px}
.tabs-text{position:absolute;top:277px;height:68px;line-height:68px;font-size:30px;color:var(--white);text-align:center}
.ticks{position:absolute;top:386px;list-style:none;font-size:15px;color:#555;line-height:42px}
.ticks li{display:flex;align-items:center;gap:12px}

/* clients */
.clients{top:3718px;height:622px;background:var(--grey-band)}
.clients .h-section{position:absolute;top:54px;width:100%}
.clients .divider{position:absolute;left:505px;top:146px}
.clients-body{position:absolute;top:200px;left:210px;width:780px;text-align:center;font-size:14px;line-height:24px;color:#555}
.avatar{position:absolute;left:530px;top:266px;width:110px;height:110px;border-radius:50%;background:linear-gradient(180deg,#c7c2bd,#6d6f73);border:5px solid var(--white)}
.quote{position:absolute;top:400px;left:140px;width:920px;text-align:center;font-size:14px;line-height:24px;color:#555}
.client-name{position:absolute;top:494px;width:100%;text-align:center;font-size:13px;font-weight:700;color:#555}
.client-co{position:absolute;top:516px;width:100%;text-align:center;font-size:13px;font-weight:700;color:var(--ink)}
.client-dots{position:absolute;top:548px;left:497px;display:flex;gap:6px}
.client-dots i{display:block;width:26px;height:5px;background:#cfcfcf}
.client-dots i.on{width:52px;background:var(--blue)}

/* quotes */
.quotes{top:4340px;height:612px;background:linear-gradient(180deg,var(--blue),var(--blue-deep))}
.quotes .h-section{position:absolute;top:44px;width:100%;color:var(--white);font-weight:700}
.quotes .divider{position:absolute;left:505px;top:155px}
.quotes-body{position:absolute;top:212px;left:210px;width:780px;text-align:center;color:var(--white);font-size:14px;line-height:24px}
.field{position:absolute;left:230px;width:737px;border:1px solid rgba(255,255,255,.8);color:var(--white);font-size:13px;padding:10px 12px}
.submit{position:absolute;left:514px;top:514px;width:146px;height:44px;background:var(--green);color:var(--white);font-size:15px;line-height:44px;text-align:center}

/* footer */
.footer{top:4952px;height:118px;background:#111}
.social{position:absolute;top:26px;width:100%;display:flex;justify-content:center;gap:8px}
.social i{display:block;width:36px;height:36px;border-radius:50%;background:var(--white)}
.copy{position:absolute;top:76px;width:100%;text-align:center;color:#ddd;font-size:14px}
</style>
</head>
<body>

<header class="section hero">
  <div class="hero-photo" role="img" aria-label="Overhead photo of a person working at a desk with a laptop"></div>
  <div class="brand"><span class="brand-dot"></span>Trade Our Goods</div>
  <nav class="nav">
    <span class="active">Home</span><span>About Us</span><span>Services</span><span>Our Work</span><span>Products</span><span>Contact</span>
  </nav>
  <p class="hero-kicker">BUILDING YOUR OWN VIRTUAL SALES TEAM</p>
  <h1 class="hero-title">JOIN<span class="sep">›</span>BUILD<span class="sep">›</span>EARN</h1>
</header>

<div class="section split-band"></div>
<div class="split">
  <div class="split-card merchants">
    <h2>MERCHANTS</h2>
    <p>Register to build your virtual sales team</p>
    <span class="split-btn">Build Sales Team</span>
  </div>
  <div class="split-card resellers">
    <h2>RESELLERS</h2>
    <p>Register to start earning money</p>
    <span class="split-btn">Earn Money now</span>
  </div>
</div>

<section class="section what">
  <h2 class="h-section center">WHAT WE DO</h2>
  <div class="divider"><span></span></div>
  <p class="what-sub center">Bringing reseller opportunities to the masses.</p>
  <p class="what-body">simply dummy text of the printing and typesetting industry. Lorem Ipsum has been the industry's standard dummy text ever since the 1500s, when an unknown printer took a galley of type and scrambled it to make a type specimen book.</p>
</section>

<section class="section why">
  <div class="why-photo" role="img" aria-label="Photo of hands typing on a laptop beside a notebook, phone and coffee cup"></div>
  <h2>WHY PICK RESELLING</h2>
  <p class="why-sub">Bringing reseller opportunities to the masses.</p>
  <ul class="why-list">
    <li>› Personal requirement for a reseller base.</li>
    <li>› Experienced reseller models that work.</li>
    <li>› Building an effective virtual sales team.</li>
    <li>› Helping SME's earn money for old rope.</li>
    <li>› Easy to generate revenue for a minimal cost.</li>
  </ul>
</section>

<section class="section blog">
  <h2 class="h-section center">BLOG POST</h2>
  <div class="divider"><span></span></div>
  <article class="post" style="left:142px">
    <div class="post-photo" role="img" aria-label="Photo of a business team meeting around a table"></div>
    <div class="post-bar"><h3>Distinctively promote access to backend</h3><div class="post-meta"><span>◷ January 13, 2015</span><span>▢ 0 Comment</span></div></div>
  </article>
  <article class="post" style="left:456px">
    <div class="post-photo" role="img" aria-label="Photo of a man working on a laptop"></div>
    <div class="post-bar"><h3>Distinctively promote access to backend</h3><div class="post-meta"><span>◷ January 13, 2015</span><span>▢ 0 Comment</span></div></div>
  </article>
  <article class="post" style="left:777px">
    <div class="post-photo" role="img" aria-label="Photo of hands reviewing charts on paper"></div>
    <div class="post-bar"><h3>Distinctively promote access to backend</h3><div class="post-meta"><span>◷ January 13, 2015</span><span>▢ 0 Comment</span></div></div>
  </article>
  <div class="dots"><i></i><i class="on"></i><i></i></div>
</section>

<section class="section how">
  <h2 class="h-section center">HOW IT WORKS</h2>
  <div class="divider on-dark"><span></span></div>
  <p class="how-body">Lorem Ipsum is simply dummy text of the printing and typesetting industry. Lorem Ipsum has been the industry's standard dummy text ever since the 1500s, when an unknown printer took</p>
  <svg class="hex-row" viewBox="0 0 1200 642" aria-hidden="true">
    <defs>
      <polygon id="hex" points="0,-50 43,-25 43,25 0,50 -43,25 -43,-25"/>
    </defs>
    <g fill="#1a8fd6">
      <use href="#hex" x="176" y="433"/><use href="#hex" x="294" y="433"/><use href="#hex" x="412" y="433"/>
    </g>
    <g fill="#8cc63f">
      <use href="#hex" x="760" y="433"/><use href="#hex" x="882" y="433"/><use href="#hex" x="1000" y="433"/>
    </g>
    <polygon points="602,348 676,391 676,475 602,518 528,475 528,391" fill="#e6e6e6"/>
    <text x="602" y="428" text-anchor="middle" font-family="Open Sans,sans-serif" font-size="20" font-weight="600" fill="#333">PROMOTE</text>
    <text x="602" y="454" text-anchor="middle" font-family="Open Sans,sans-serif" font-size="20" font-weight="600" fill="#333">AND EARN</text>
    <g fill="#fff" stroke="#fff" stroke-width="2">
      <circle cx="166" cy="420" r="5"/><circle cx="186" cy="420" r="5"/>
      <rect x="158" y="430" width="16" height="16" stroke="none"/><rect x="178" y="430" width="16" height="16" stroke="none"/>
      <path d="M282 446 L306 420 M294 420 h12 v12" fill="none" stroke-width="4"/>
      <rect x="400" y="416" width="24" height="32" fill="none"/>
      <path d="M405 426h14M405 433h14M405 440h14" fill="none"/>
      <circle cx="756" cy="428" r="10" fill="none" stroke-width="4"/><path d="M763 436l10 10" stroke-width="5"/>
      <circle cx="878" cy="422" r="8" stroke="none"/><path d="M864 448a14 12 0 0 1 28 0z" stroke="none"/>
      <circle cx="992" cy="422" r="6" stroke="none"/><circle cx="1008" cy="422" r="6" stroke="none"/>
      <path d="M982 446a10 10 0 0 1 20 0zM998 446a10 10 0 0 1 20 0z" stroke="none"/>
    </g>
  </svg>
  <span class="hex-label" style="left:176px">Merchants</span>
  <span class="hex-label" style="left:294px">Payment</span>
  <span class="hex-label" style="left:412px">Listing</span>
  <span class="hex-label" style="left:760px">Search</span>
  <span class="hex-label" style="left:882px">Register</span>
  <span class="hex-label" style="left:1000px">Resellers</span>
</section>

<section class="section benefits">
  <h2 class="h-section center">BENEFITS FOR EVERYONE</h2>
  <div class="divider"><span></span></div>
  <svg class="ribbon" viewBox="0 0 1200 68" aria-hidden="true">
    <polygon points="270,0 588,0 588,68 270,68 237,34" fill="#1a8fd6"/>
    <polygon points="588,0 906,0 940,34 906,68 588,68" fill="#8cc63f"/>
  </svg>
  <div class="tabs-text" style="left:237px;width:351px">MERCHANTS</div>
  <div class="tabs-text" style="left:588px;width:352px">RESELLERS</div>
  <ul class="ticks" style="left:305px">
    <li><svg width="16" height="14" viewBox="0 0 16 14"><path d="M1 7l5 5 9-11" fill="none" stroke="#1a8fd6" stroke-width="2.5"/></svg>Additional Stream of Income</li>
    <li><svg width="16" height="14" viewBox="0 0 16 14"><path d="M1 7l5 5 9-11" fill="none" stroke="#1a8fd6" stroke-width="2.5"/></svg>Infrastructure in Place</li>
    <li><svg width="16" height="14" viewBox="0 0 16 14"><path d="M1 7l5 5 9-11" fill="none" stroke="#1a8fd6" stroke-width="2.5"/></svg>No Additional Cost</li>
    <li><svg width="16" height="14" viewBox="0 0 16 14"><path d="M1 7l5 5 9-11" fill="none" stroke="#1a8fd6" stroke-width="2.5"/></svg>Expand Product Suite</li>
    <li><svg width="16" height="14" viewBox="0 0 16 14"><path d="M1 7l5 5 9-11" fill="none" stroke="#1a8fd6" stroke-width="2.5"/></svg>Reach New Target Markets</li>
  </ul>
  <ul class="ticks" style="left:632px">
    <li><svg width="16" height="14" viewBox="0 0 16 14"><path d="M1 7l5 5 9-11" fill="none" stroke="#8cc63f" stroke-width="2.5"/></svg>Additional Stream of Income</li>
    <li><svg width="16" height="14" viewBox="0 0 16 14"><path d="M1 7l5 5 9-11" fill="none" stroke="#8cc63f" stroke-width="2.5"/></svg>Infrastructure in Place</li>
    <li><svg width="16" height="14" viewBox="0 0 16 14"><path d="M1 7l5 5 9-11" fill="none" stroke="#8cc63f" stroke-width="2.5"/></svg>No Additional Cost</li>
    <li><svg width="16" height="14" viewBox="0 0 16 14"><path d="M1 7l5 5 9-11" fill="none" stroke="#8cc63f" stroke-width="2.5"/></svg>Expand Product Suite</li>
    <li><svg width="16" height="14" viewBox="0 0 16 14"><path d="M1 7l5 5 9-11" fill="none" stroke="#8cc63f" stroke-width="2.5"/></svg>Reach New Target Markets</li>
  </ul>
</section>

<section class="section clients">
  <h2 class="h-section center">OUR CLIENTS</h2>
  <div class="divider"><span></span></div>
  <p class="clients-body">Lorem Ipsum is simply dummy text of the printing and typesetting industry. Lorem Ipsum has been the industry's standard dummy text ever since the 1500s, when an unknown printer took</p>
  <div class="avatar" role="img" aria-label="Client portrait photo"></div>
  <p class="quote">A wonderful serenity has taken possession of my entire soul, like these sweet mornings of spring which I enjoy with my whole heart. I am alone, and feel the charm of existence in this spot, which was created for the bliss of souls like mine. I am so happy.</p>
  <p class="client-name">JOHN DOE</p>
  <p class="client-co">Norvane Tech Company</p>
  <div class="client-dots"><i class="on"></i><i></i><i></i></div>
</section>

<section class="section quotes">
  <h2 class="h-section center">FREE QUOTES</h2>
  <div class="divider on-blue"><span></span></div>
  <p class="quotes-body">Lorem Ipsum is simply dummy text of the printing and typesetting industry. Lorem Ipsum has been the industry's standard dummy text ever since the 1500s, when an unknown printer took</p>
  <div class="field" style="top:273px;height:45px">Enter Name</div>
  <div class="field" style="top:331px;height:44px">Enter Email</div>
  <div class="field" style="top:385px;height:102px"></div>
  <div class="submit">Submit Now</div>
</section>

<footer class="section footer">
  <div class="social"><i></i><i></i><i></i><i></i><i></i></div>
  <p class="copy">© 2016 Tradeourgoods.com . All Rights Reserved</p>
</footer>

</body>
</html>
```